Tolbi Fund Map Tracker

Consumers track their three credit scores. I have sent an illustration after one update of their credit scores. Many consumers will have a dozen updates during one year. I would like to show a history of the last 24 months. Put together a design that is attractive and easy to look at and follow. I have updated some ideas for graphs (Apr 5, 2022)

Target Market(s)

Consumers tracking their credit scores

Coding

Coded - Design and coding required

Number of Pages Required

1 page

Colors
0054AA
0677BA
7BADD7
CADEEF
E8F1F8
00AB8E
00BBA5
67D7C9
C6EFE9
E9F9F6

Requirements
Must have
• Scores from 350 to 850 pon the left hand side - dates the credit scores were pulled at the bottom on the x axis
Nice to have
• 3 digit credit score for each of the three scores /

```html
<!DOCTYPE html>
<html lang="en">
<head>
<meta charset="utf-8">
<title>Tolbi Fund Map – Credit Score History</title>
<link href="https://fonts.googleapis.com/css2?family=Poppins:wght@400;500;700;800&display=swap" rel="stylesheet">
<style>
  :root {
    --page-bg: #ffffff;
    --header-bg: #f9f9f9;
    --brand-blue: #1e5fd6;
    --title-blue: #0a0ae8;
    --axis-green: #0a9a47;
    --rule: #b5b5b5;
    --grid: #e6e6e6;
    --tick-text: #777777;
    --bureau-a-fill: #d6e2fd;
    --bureau-a-line: #5a7ee0;
    --bureau-b-fill: #a6fde0;
    --bureau-b-line: #22d18e;
    --panel: #fdfdfd;
  }
  * { margin: 0; padding: 0; box-sizing: border-box; }
  html, body { width: 1200px; height: 891px; overflow: hidden; background: var(--page-bg); font-family: "Poppins", sans-serif; }
  .canvas { position: relative; width: 1200px; height: 891px; }
  .site-header { position: absolute; left: 0; top: 0; width: 1200px; height: 99px; background: var(--header-bg); }
  .brand { position: absolute; left: 89px; top: 40px; display: flex; align-items: center; gap: 10px; }
  .brand-mark { width: 30px; height: 30px; background: var(--brand-blue); border-radius: 3px; }
  .brand-name { font-size: 17px; font-weight: 500; color: var(--brand-blue); }
  .page-title { position: absolute; left: 84px; top: 156px; font-size: 26px; font-weight: 800; color: var(--title-blue); letter-spacing: -0.3px; }
  .title-rule { position: absolute; left: 84px; top: 196px; width: 1033px; height: 1px; background: var(--rule); }
  .axis-title-y { position: absolute; left: 93px; top: 458px; transform: translate(-50%, -50%) rotate(-90deg); font-size: 20px; font-weight: 800; color: var(--title-blue); white-space: nowrap; }
  .axis-title-x { position: absolute; left: 617px; top: 768px; transform: translate(-50%, -50%); font-size: 20px; font-weight: 800; color: var(--axis-green); white-space: nowrap; }
  .score-chart { position: absolute; left: 0; top: 0; }
  .grid-line { stroke: var(--grid); stroke-width: 1; }
  .tick-label { font-family: "Poppins", sans-serif; font-size: 12px; fill: var(--tick-text); }
  .legend-label { font-family: "Poppins", sans-serif; font-size: 16px; fill: var(--tick-text); }
  .bar-a { fill: var(--bureau-a-fill); stroke: var(--bureau-a-line); stroke-width: 1.5; }
  .bar-b { fill: var(--bureau-b-fill); stroke: var(--bureau-b-line); stroke-width: 1.5; }
</style>
</head>
<body>
<div class="canvas">
  <header class="site-header">
    <div class="brand">
      <span class="brand-mark"></span>
      <span class="brand-name">Tolbi Fund Map</span>
    </div>
  </header>

  <h1 class="page-title">MY CREDIT SCORE HISTORY</h1>
  <div class="title-rule"></div>

  <svg class="score-chart" width="1200" height="891" viewBox="0 0 1200 891" aria-label="Credit score history by month">
    <rect x="113" y="225" width="1003" height="524" fill="var(--panel)"/>

    <g class="legend">
      <rect class="bar-a" x="451" y="239" width="36" height="17"/>
      <text class="legend-label" x="495" y="253">VERIDATA</text>
      <rect class="bar-b" x="581" y="239" width="36" height="17"/>
      <text class="legend-label" x="625" y="253">CRESTLINE</text>
    </g>

    <g class="grid">
      <line class="grid-line" x1="168" y1="265" x2="1108" y2="265"/>
      <line class="grid-line" x1="168" y1="337.3" x2="1108" y2="337.3"/>
      <line class="grid-line" x1="168" y1="409.8" x2="1108" y2="409.8"/>
      <line class="grid-line" x1="168" y1="482.4" x2="1108" y2="482.4"/>
      <line class="grid-line" x1="168" y1="554.9" x2="1108" y2="554.9"/>
      <line class="grid-line" x1="168" y1="627.5" x2="1108" y2="627.5"/>
      <line class="grid-line" x1="168" y1="700" x2="1108" y2="700"/>
      <line class="grid-line" x1="176" y1="265" x2="176" y2="708"/>
      <line class="grid-line" x1="253.7" y1="265" x2="253.7" y2="708"/>
      <line class="grid-line" x1="331.3" y1="265" x2="331.3" y2="708"/>
      <line class="grid-line" x1="409" y1="265" x2="409" y2="708"/>
      <line class="grid-line" x1="486.7" y1="265" x2="486.7" y2="708"/>
      <line class="grid-line" x1="564.3" y1="265" x2="564.3" y2="708"/>
      <line class="grid-line" x1="642" y1="265" x2="642" y2="708"/>
      <line class="grid-line" x1="719.7" y1="265" x2="719.7" y2="708"/>
      <line class="grid-line" x1="797.3" y1="265" x2="797.3" y2="708"/>
      <line class="grid-line" x1="875" y1="265" x2="875" y2="708"/>
      <line class="grid-line" x1="952.7" y1="265" x2="952.7" y2="708"/>
      <line class="grid-line" x1="1030.3" y1="265" x2="1030.3" y2="708"/>
      <line class="grid-line" x1="1108" y1="265" x2="1108" y2="708"/>
    </g>

    <g class="y-ticks" text-anchor="end">
      <text class="tick-label" x="150" y="269">900</text>
      <text class="tick-label" x="150" y="341">800</text>
      <text class="tick-label" x="150" y="414">700</text>
      <text class="tick-label" x="150" y="486">600</text>
      <text class="tick-label" x="150" y="559">500</text>
      <text class="tick-label" x="150" y="631">400</text>
      <text class="tick-label" x="150" y="704">300</text>
    </g>

    <g class="bars">
      <rect class="bar-a" x="185.5" y="663.7" width="27" height="36.3"/>
      <rect class="bar-b" x="216.7" y="642" width="27" height="58"/>
      <rect class="bar-a" x="263.2" y="583.9" width="27" height="116.1"/>
      <rect class="bar-b" x="294.4" y="569.4" width="27" height="130.6"/>
      <rect class="bar-a" x="340.8" y="642" width="27" height="58"/>
      <rect class="bar-b" x="372" y="482.4" width="27" height="217.6"/>
      <rect class="bar-a" x="418.5" y="409.8" width="27" height="290.2"/>
      <rect class="bar-b" x="449.7" y="642" width="27" height="58"/>
      <rect class="bar-a" x="496.2" y="265" width="27" height="435"/>
      <rect class="bar-b" x="527.4" y="409.8" width="27" height="290.2"/>
      <rect class="bar-a" x="573.8" y="301.3" width="27" height="398.7"/>
      <rect class="bar-b" x="605" y="663.7" width="27" height="36.3"/>
      <rect class="bar-a" x="651.5" y="446.1" width="27" height="253.9"/>
      <rect class="bar-b" x="682.7" y="446.1" width="27" height="253.9"/>
      <rect class="bar-a" x="729.2" y="446.1" width="27" height="253.9"/>
      <rect class="bar-b" x="760.4" y="627.5" width="27" height="72.5"/>
      <rect class="bar-a" x="806.8" y="373.6" width="27" height="326.4"/>
      <rect class="bar-b" x="838" y="373.6" width="27" height="326.4"/>
      <rect class="bar-a" x="884.5" y="337.3" width="27" height="362.7"/>
      <rect class="bar-b" x="915.7" y="337.3" width="27" height="362.7"/>
      <rect class="bar-a" x="962.2" y="554.9" width="27" height="145.1"/>
      <rect class="bar-b" x="993.4" y="482.4" width="27" height="217.6"/>
      <rect class="bar-a" x="1039.8" y="627.5" width="27" height="72.5"/>
      <rect class="bar-b" x="1071" y="265" width="27" height="435"/>
    </g>

    <g class="x-ticks" text-anchor="middle">
      <text class="tick-label" x="214.8" y="736">JAN</text>
      <text class="tick-label" x="292.5" y="736">FEB</text>
      <text class="tick-label" x="370.1" y="736">MAR</text>
      <text class="tick-label" x="447.8" y="736">APR</text>
      <text class="tick-label" x="525.5" y="736">MAY</text>
      <text class="tick-label" x="603.1" y="736">JUN</text>
      <text class="tick-label" x="680.8" y="736">JUL</text>
      <text class="tick-label" x="758.5" y="736">AUG</text>
      <text class="tick-label" x="836.1" y="736">SEP</text>
      <text class="tick-label" x="913.8" y="736">OCT</text>
      <text class="tick-label" x="991.5" y="736">NOV</text>
      <text class="tick-label" x="1069.1" y="736">DEC</text>
    </g>
  </svg>

  <div class="axis-title-y">Credit Score</div>
  <div class="axis-title-x">Credit Pull Date</div>
</div>
</body>
</html>
```